Harbour Physiotherapy business card design

We need a fresh, new business card design for our physiotherapy clinic Harbour Physiotherapy

Will attach logo soon we had logo designed from our last project

Industry/Entity Type

Physical Therapy

Contact Information for Business Card

On front
Needs our logo, contact details:
58 Wilmot Street Glenfield NSW 2167
Ph/f: 02 9418 2753
info@harbourphysiotherapy.com.au

Requirements
Must have
• On the back of the card needs to have area to write down follow up appointments
• On front
• Needs our logo
• The colours have to be the colours in our logo which are: sky blue, black and white
• Font to be same as our logo please
• We want the card to look simple, not too cluttered but to the point
Should not have
• We don't need any extra pictures other than our logo

```html
<!DOCTYPE html>
<html lang="en">
<head>
<meta charset="utf-8">
<title>Harbour Physiotherapy – Business Card</title>
<link href="https://fonts.googleapis.com/css2?family=Exo+2:wght@500;700&family=Open+Sans:wght@400;600&display=swap" rel="stylesheet">
<style>
  :root {
    --stage: #4b4b4d;
    --card: #ffffff;
    --brand-blue: #1e7fd6;
    --deep-blue: #2b35a8;
    --mid-blue: #1f6fc4;
    --bright-blue: #1f62cc;
    --charcoal: #3b3b3e;
    --rule: #3a3a3a;
  }
  * { box-sizing: border-box; margin: 0; padding: 0; }
  html, body { width: 1105px; height: 1200px; overflow: hidden; }
  body { background: var(--stage); position: relative; font-family: "Open Sans", sans-serif; }

  .card {
    position: absolute; left: 196px; width: 720px; height: 412px;
    background: var(--card); border-radius: 18px; overflow: hidden;
  }
  .card--front { top: 146px; }
  .card--back { top: 602px; }

  .front-band {
    position: absolute; left: 0; top: 186px; width: 100%; height: 226px;
    background: linear-gradient(90deg, var(--deep-blue) 0%, var(--bright-blue) 60%, var(--deep-blue) 100%);
    border-top: 14px solid var(--charcoal);
  }

  .brand {
    position: absolute; left: 44px; top: 92px;
    display: flex; align-items: center; gap: 14px;
  }
  .brand__dot { width: 26px; height: 26px; border-radius: 50%; background: var(--brand-blue); }
  .brand__name {
    font-family: "Open Sans", sans-serif; font-weight: 600; font-size: 34px;
    line-height: 1.05; color: var(--brand-blue);
  }

  .contact {
    position: absolute; right: 26px; top: 206px; text-align: right; color: #fff;
    font-size: 19px; line-height: 1.25;
  }
  .contact__name { font-size: 25px; font-weight: 600; }
  .contact__role { margin-bottom: 18px; }
  .contact__line { margin-top: 7px; }
  .contact__label { font-weight: 600; margin-right: 6px; }

  .appointments__title {
    position: absolute; top: 42px; width: 100%; text-align: center;
    font-family: "Exo 2", sans-serif; font-weight: 700; font-size: 26px; color: var(--mid-blue);
    letter-spacing: 0.5px;
  }
  .slot { position: absolute; left: 44px; width: 622px; height: 30px; }
  .slot__date, .slot__time {
    position: absolute; bottom: 0; border-bottom: 1.5px solid var(--rule);
    font-family: "Exo 2", sans-serif; font-weight: 500; font-size: 20px; color: var(--mid-blue);
    padding-bottom: 2px; height: 30px;
  }
  .slot__date { left: 0; width: 333px; }
  .slot__time { left: 356px; width: 266px; }
  .slot__ampm { position: absolute; right: 0; bottom: 2px; font-size: 16px; }

  .notice {
    position: absolute; left: 0; top: 348px; width: 100%; height: 47px;
    background: var(--mid-blue); color: #fff; text-align: center;
    font-family: "Exo 2", sans-serif; font-size: 13.5px; line-height: 1.3; padding-top: 5px;
  }
</style>
</head>
<body>

<section class="card card--front">
  <div class="front-band" role="img" aria-label="Decorative blue and charcoal band behind the contact details"></div>

  <div class="brand">
    <span class="brand__dot"></span>
    <p class="brand__name">Harbour<br>Physiotherapy</p>
  </div>

  <div class="contact">
    <p class="contact__name">Daniel Hart</p>
    <p class="contact__role">CEO/Founder</p>
    <p class="contact__line"><span class="contact__label">Ph/Fax</span>02 9418 2753</p>
    <p class="contact__line">info@harbourphysiotherapy.com.au</p>
    <p class="contact__line">www.harbourphysiotherapy.com.au</p>
    <p class="contact__line">58 Wilmot Street Glenfield, NSW 2167</p>
  </div>
</section>

<section class="card card--back">
  <h2 class="appointments__title">Next Appointment</h2>

  <div class="slot" style="top:100px">
    <div class="slot__date">Date :</div>
    <div class="slot__time">Time :<span class="slot__ampm">AM/PM</span></div>
  </div>
  <div class="slot" style="top:182px">
    <div class="slot__date">Date :</div>
    <div class="slot__time">Time :<span class="slot__ampm">AM/PM</span></div>
  </div>
  <div class="slot" style="top:264px">
    <div class="slot__date">Date :</div>
    <div class="slot__time">Time :<span class="slot__ampm">AM/PM</span></div>
  </div>

  <p class="notice">Please give me 24 hours notice if you are unable to keep your<br>appointment or a cancellation fee may be charged.</p>
</section>

</body>
</html>
```